Technology research organisation needs a white paper redesign

Goal: Redesign the current "Platform Compass" white paper using our Pellara Insights branding.
- The design should promote a brand which is independent, has trusted advisors, is down to earth, has plain english advice based on solid research.
- Prefer a one column layout which is easy to read and has enough space for call outs on either left or right hand side.
- A4 size document will be distributed in PDF format
- Feel free to re-design existing graphs, tables, change images, headers and footers.
- Audience: HR Directors, CIO's & CFO's
- Must use our standard colour palette, see attached.
- The font used is company name: Frutiger LT 57 CN
- Should be inline with our website: pellarainsights.com.au
Design must allow for:
* Front Page
* Main content
* Contact details, about Pellara Insights & author example content can be found http://pellarainsights.com.au/about/
Output:
- All adobe design files
- Images, Fonts
Target Market(s)
Audience: HR Directors, CIO's & CFO's most likely 40+
Industry/Entity Type
It Company
Font styles to use
Other font styles liked:
- Frutiger LT 57 CN
Look and feel

```html
<!DOCTYPE html>
<html lang="en">
<head>
<meta charset="utf-8">
<title>Pellara Insights – Platform Compass white paper spreads</title>
<link rel="stylesheet" href="https://fonts.googleapis.com/css2?family=Open+Sans:wght@400;600;700&display=swap">
<style>
  :root{
    --red:#ee3524;
    --grey:#c6c6c6;
    --dark:#383838;
    --sand:#e3d79f;
    --lime:#c3d02a;
    --title:#c4c4c4;
    --ink:#444;
    --band:#f5f6f8;
    --paper:#fff;
    --bg:#fff;
  }
  *{box-sizing:border-box;margin:0;padding:0}
  html,body{width:855px;height:1200px;overflow:hidden;background:var(--bg)}
  body{font-family:"Open Sans",Arial,sans-serif;color:var(--ink)}
  .stage{position:relative;width:900px;height:1263px;transform:scale(.95);transform-origin:0 0}
  .spread{position:absolute;left:31px;width:842px;height:595px;background:var(--paper);
    box-shadow:0 1px 4px rgba(0,0,0,.28);overflow:hidden}
  .spread--top{top:28px}
  .spread--bottom{top:645px}
  .spread::after{content:"";position:absolute;left:421px;top:0;bottom:0;width:1px;background:#e2e2e2}
  .page{position:absolute;top:0;width:421px;height:595px}
  .page--left{left:0}
  .page--right{left:421px}
  .sq{position:absolute}
  .sq--grey{background:var(--grey)}
  .sq--sand{background:var(--sand)}
  .sq--red{background:var(--red)}
  .sq--dark{background:var(--dark)}
  .page-title{position:absolute;top:32px;font-size:26px;line-height:31px;font-weight:700;color:var(--title);letter-spacing:.2px}
  .page--left .page-title{right:43px;text-align:right}
  .page--right .page-title{left:43px}
  .body-copy{position:absolute;top:122px;width:265px;font-size:7.9px;line-height:16px;letter-spacing:.35px;text-align:justify}
  .page--left .body-copy{left:114px}
  .page--right .body-copy{left:43px}
  .body-copy p{margin-bottom:6px}
  .body-copy b{font-weight:700;color:#333}
  .accent{color:var(--red)}
  .rule-short{width:29px;height:1px;background:var(--red);margin:13px 0 9px}
  .section-label{position:absolute;font-size:8.8px;font-weight:700;color:#333;letter-spacing:.3px}
  .steps{position:absolute;left:114px;top:414px;display:flex;gap:15px}
  .step{width:41px;text-align:center}
  .step svg{display:block;width:41px;height:41px}
  .step span{display:block;margin-top:5px;font-size:6.6px;line-height:10px;color:#333;white-space:nowrap;margin-left:-10px;margin-right:-10px}
  .motif{position:absolute;left:160px;top:362px;width:100px;height:105px;border-radius:50%;
    background:radial-gradient(circle,rgba(0,0,0,.025),rgba(0,0,0,0) 70%)}
  .footer{position:absolute;bottom:0;height:50px;width:325px}
  .page--left .footer{left:54px}
  .page--right .footer{left:43px}
  .footer .brand{position:absolute;top:0;font-size:7.6px;font-weight:700;letter-spacing:.3px;color:#222}
  .footer .brand .accent{color:var(--red)}
  .page--left .footer .brand{right:0}
  .page--right .footer .brand{left:0}
  .footer .line{position:absolute;top:13px;left:0;width:100%;height:1px;background:var(--red)}
  .footer .tag{position:absolute;top:19px;font-size:7.4px;letter-spacing:.4px;color:#333}
  .footer .num{position:absolute;top:19px;font-size:7.4px;font-weight:700;color:#333}
  .page--left .footer .tag{right:0}
  .page--left .footer .num{left:0}
  .page--right .footer .tag{left:0}
  .page--right .footer .num{right:0}
  .band{position:absolute;left:0;top:325px;width:842px;height:180px;background:var(--band)}
  .chevron{position:absolute;top:354px;width:121px;height:54px}
  .chevron svg{position:absolute;inset:0}
  .chevron span{position:relative;display:flex;align-items:center;justify-content:center;height:100%;
    color:#fff;font-size:9px;font-weight:700;letter-spacing:.4px;padding-left:4px}
  .checklist{position:absolute;top:420px;list-style:none;font-size:7.4px;line-height:10px;color:#333;letter-spacing:.2px}
  .checklist li{position:relative;padding-left:14px;margin-bottom:7px}
  .checklist li::before{content:"";position:absolute;left:0;top:1px;width:8px;height:8px;background:var(--grey)}
</style>
</head>
<body>
<div class="stage">

  <section class="spread spread--top">
    <article class="page page--left">
      <div class="sq sq--grey" style="left:18px;top:47px;width:32px;height:31px"></div>
      <div class="sq sq--sand" style="left:64px;top:22px;width:32px;height:32px"></div>
      <div class="sq sq--red" style="left:63px;top:67px;width:11px;height:11px"></div>
      <div class="sq sq--dark" style="left:89px;top:63px;width:25px;height:25px"></div>
      <h1 class="page-title">THE SOFTWARE<br>SELECTION PROCESS</h1>
      <div class="body-copy">
        <p>Pellara Insights recommends organisations follow a five step process for software selection.</p>
        <p>A formal <b>project kick off</b> is a good project management practice to establish terms of reference, governance, key resources and a plan.</p>
        <p>The critical key to success begins with the <b>Strategy Review</b>.</p>
        <p>A strategic review needs to look at understanding your Business and HR strategic plans while at the same time looking to your current and planned HR Technology landscape and its alignment with the business strategy.</p>
        <p>Understanding and linking an organisation’s business strategy to the “why” of purchasing software is critical. A clear and detailed understanding of the business strategy and its drivers is a must.</p>
        <p>This not only provides a clear roadmap but it also helps build a rock solid business case.</p>
      </div>
      <h2 class="section-label" style="left:114px;top:393px">SOFTWARE SELECTION</h2>
      <div class="steps">
        <div class="step">
          <svg viewBox="0 0 41 41"><rect width="41" height="41" fill="var(--red)"/><polygon points="14,11 30,20.5 14,30" fill="#fff"/></svg>
          <span>Project<br>Kickoff</span>
        </div>
        <div class="step">
          <svg viewBox="0 0 41 41"><rect width="41" height="41" fill="var(--grey)"/><circle cx="13" cy="20.5" r="3" fill="#fff"/><circle cx="20.5" cy="20.5" r="3" fill="#fff"/><circle cx="28" cy="20.5" r="3" fill="#fff"/></svg>
          <span>Strategy<br>Review</span>
        </div>
        <div class="step">
          <svg viewBox="0 0 41 41"><rect width="41" height="41" fill="var(--lime)"/><polyline points="10,21 17,28 31,13" fill="none" stroke="#fff" stroke-width="5"/></svg>
          <span>Confirm<br>Requirements</span>
        </div>
        <div class="step">
          <svg viewBox="0 0 41 41"><rect width="41" height="41" fill="var(--sand)"/><rect x="11" y="11" width="4" height="19" fill="#fff"/><polygon points="30,11 30,30 17,20.5" fill="#fff"/></svg>
          <span>Market Review<br>&amp; Roadmap</span>
        </div>
        <div class="step">
          <svg viewBox="0 0 41 41"><rect width="41" height="41" fill="var(--dark)"/><rect x="9" y="9" width="23" height="23" fill="none" stroke="#fff" stroke-width="3"/><rect x="14" y="14" width="13" height="13" fill="#fff"/></svg>
          <span>Selection</span>
        </div>
      </div>
      <footer class="footer">
        <div class="brand"><span class="accent">PELLARA</span> INSIGHTS</div>
        <div class="line"></div>
        <div class="num">8</div>
        <div class="tag">MARKET INTELLIGENCE &amp; ADVISORY</div>
      </footer>
    </article>

    <article class="page page--right">
      <div class="sq sq--sand" style="left:325px;top:22px;width:32px;height:32px"></div>
      <div class="sq sq--dark" style="left:308px;top:63px;width:25px;height:25px"></div>
      <div class="sq sq--red" style="left:347px;top:67px;width:11px;height:11px"></div>
      <div class="sq sq--grey" style="left:371px;top:47px;width:32px;height:31px"></div>
      <h1 class="page-title">UNDERSTANDING<br>REQUIREMENTS</h1>
      <div class="body-copy">
        <p>The requirements review looks at what your organisation wants from a software solution.</p>
        <p>As well as creating a “laundry list” of requirements, articulate the high-level requirements—the ones that support your organisation’s unique value proposition.</p>
        <p>Remember most vendors who have been in the Australian market-place for a few years have a solid payroll engine. Don’t focus on general requirements—look for unique requirements.</p>
        <p>If you are in doubt about the vendor capabilities conduct customer reference checks.</p>
      </div>
      <div class="motif" role="img" aria-label="Faint decorative motif of linked circles"></div>
      <footer class="footer">
        <div class="brand"><span class="accent">PELLARA</span> INSIGHTS</div>
        <div class="line"></div>
        <div class="tag">MARKET INTELLIGENCE &amp; ADVISORY</div>
        <div class="num">9</div>
      </footer>
    </article>
  </section>

  <section class="spread spread--bottom">
    <div class="band"></div>
    <article class="page page--left">
      <div class="sq sq--grey" style="left:18px;top:48px;width:32px;height:31px"></div>
      <div class="sq sq--red" style="left:64px;top:23px;width:32px;height:32px"></div>
      <div class="sq sq--red" style="left:63px;top:69px;width:11px;height:11px"></div>
      <div class="sq sq--dark" style="left:89px;top:64px;width:25px;height:25px"></div>
      <h1 class="page-title">MARKET REVIEW<br>&amp; ROADMAP</h1>
      <div class="body-copy">
        <p>The <span class="accent">market review</span> needs to identify suitable vendors for your organisation to review in more detail.</p>
        <p>Pellara Insights has a full list of vendor’s offerings for the Austra-lian market.</p>
        <p>Many times this can only be accomplished through an RFI allowing a comparison of how well their solutions will address your mandatory and key business requirements.</p>
        <div class="rule-short"></div>
        <p>Your <span class="accent">roadmap</span> needs to show not just what your organisation will be implementing but when and how. This can be difficult but is critical as these activities extend over multiple years.</p>
      </div>
      <h2 class="section-label" style="left:114px;top:335px">ROADMAP</h2>
      <div class="chevron" style="left:114px">
        <svg viewBox="0 0 121 54"><polygon points="0,0 109,0 121,27 109,54 0,54" fill="var(--red)"/></svg>
        <span>PREPARATION</span>
      </div>
      <div class="chevron" style="left:257px">
        <svg viewBox="0 0 121 54"><polygon points="0,0 109,0 121,27 109,54 0,54 12,27" fill="var(--red)"/></svg>
        <span>STREAM 1</span>
      </div>
      <ul class="checklist" style="left:257px">
        <li>Payroll &amp; Core HRIS</li>
        <li>Business Intelligence<br>&amp; Reporting</li>
        <li>Recruitment<br>&amp; Onboarding</li>
      </ul>
      <footer class="footer">
        <div class="brand"><span class="accent">PELLARA</span> INSIGHTS</div>
        <div class="line"></div>
        <div class="num">10</div>
        <div class="tag">MARKET INTELLIGENCE &amp; ADVISORY</div>
      </footer>
    </article>

    <article class="page page--right">
      <div class="sq sq--red" style="left:325px;top:23px;width:32px;height:32px"></div>
      <div class="sq sq--dark" style="left:308px;top:64px;width:25px;height:25px"></div>
      <div class="sq sq--red" style="left:347px;top:69px;width:11px;height:11px"></div>
      <div class="sq sq--grey" style="left:371px;top:48px;width:32px;height:31px"></div>
      <h1 class="page-title">SELECTION<br>PROCESS</h1>
      <div class="body-copy">
        <p>The <span class="accent">selection process</span> is the final phase. The main tool used to manage the final selection is a typical RFP process with one signifi-cant variation – prototyping and scripted demonstrations.</p>
        <p>There is only so much the RFP response and marketing demonstra-tions can show you.</p>
        <p>The ability to “see through” the demonstration is paramount to understanding how well the solution and the vendor will fit your organisation.</p>
        <p>By conducting detailed demonstrations the reliance on assumptions is removed. You can see and feel how the solution will operate.</p>
      </div>
      <div class="chevron" style="left:43px">
        <svg viewBox="0 0 121 54"><polygon points="0,0 109,0 121,27 109,54 0,54 12,27" fill="var(--red)"/></svg>
        <span>STREAM 2</span>
      </div>
      <div class="chevron" style="left:185px">
        <svg viewBox="0 0 121 54"><polygon points="0,0 109,0 121,27 109,54 0,54 12,27" fill="var(--red)"/></svg>
        <span>STREAM 3</span>
      </div>
      <ul class="checklist" style="left:43px">
        <li>OH&amp;S</li>
        <li>Benefits Managment</li>
      </ul>
      <ul class="checklist" style="left:185px">
        <li>Performance Management</li>
        <li>Remuneration and Salary<br>Planning</li>
        <li>Learning Management</li>
        <li>Succession Planning</li>
      </ul>
      <footer class="footer">
        <div class="brand"><span class="accent">PELLARA</span> INSIGHTS</div>
        <div class="line"></div>
        <div class="tag">MARKET INTELLIGENCE &amp; ADVISORY</div>
        <div class="num">11</div>
      </footer>
    </article>
  </section>

</div>
</body>
</html>
```